We need a .psd design for a store we are creating called Bright Pouches. I will need only the main home page designed.

The store will be an eCommerce website that sells custom printed men's wallets. Customers will come onto the website and be able to upload their own images or add text to the front, back and inside of the wallet. We will initially be launching with one wallet style and will be expanding our range in the future for now the only images of a wallet on the website should be of the style attached.

There will be multiple templates that a customer can choose and edit the design of so there will effectively be a large number of products on display in the store. However, on the homepage there should just be a couple of featured products and the main emphasis should be on the features of the wallet/website and links to other areas of the website (customise your own wallet, edit our templates, bespoke designer wallets).

For the styling of the website, it needs to be funky and fresh with lots of colour. The logo of the website is attached and the styling should mirror the logo style.

The main features of the website should be on the home page. These features are:
- 5 year money back guarantee on wallet
- High quality, durable leather, made to last
- customer can upload photo and edit them online with our online picture editor
- 3d mockup of the wallet as you are designing it to show what it looks like with custom images on
- Edit any of our ready made wallet designs

Features of this wallet may be used as well - these can be viewed on "Image 6" of the attached product image .psd files.

Attached are the logo for the website and the wallet product photos. The product photos are provided in .psd format and have smart objects so that you can add any image to the front/inside of the wallets for any images on the website you create. Fee free to edit them and use them for banner images and feature images however you feel necessary.

The term "what does you wallet say about you" should be used as this is a tagline for most of the marketing - based on the fact that the wallets are personalised to each individual they will show off that individuals personality and what they like.

The eventual website will be hosted on cartnest and will more than likely use the "StallKit" theme. This is a highly adaptable theme and examples of the layout styles for the homepage can be found here: http://reef.lindolayouts.example/cartnest/stallkit-intro/?storefront=pixora-assets however i do not want you to just copy a ready made template and stick some stock photos in - I only want one page designing here, put the effort in with the banners and feature images and you'll win this.

Any images that you create for hero sliders/banners should be provided in .psd format so that they can be edited as necessary in the future. A newsletter popup should also be designed as the website will have postwren integration, the newsletter popup is a 500 x 750 image that pops up with a message saying "subscribe to our newsletter and get 10% off your next order".

There should also be an area of the page that has customer testimonials.

Target Market(s)

Males, aged 18 - 45

Industry/Entity Type

Retail

Number of Pages Required

1 page

Font styles to use
Serif
Decorative
Script

Colors

Designer to choose colors to be used in the design.

Requirements
Must have
• Vibrant and uplifting feel to the website
• Design which reflects the logo
• Features of the website and wallets should feature prominently on the homepage (but not in banner/hero image)
Nice to have
• hipster/geek/easygoing vibe
• Images that have used the wallet .psd files and have different designs on them showing customers that anything can be printed on the wallets
• Custom images/styles for the featured images and main banner.
Should not have
• - Boring images
• - Stock Photos
• - Mundane feel
• - Square block style images - try putting images in circles or geometric shapes with colours, just adding a stock photo to some "lorem Ipsum" text will not win you this contest

```html
<!DOCTYPE html>
<html lang="en">
<head>
<meta charset="utf-8">
<title>Bright Pouches — Home</title>
<link href="https://fonts.googleapis.com/css2?family=Baloo+2:wght@700;800&family=Montserrat:wght@600;700;800&family=Open+Sans:wght@400;600;700&display=swap" rel="stylesheet">
<style>
:root{
  --ink:#1a1a1a;
  --white:#ffffff;
  --grey-bg:#f1f1f1;
  --card:#efefef;
  --red:#ec2a3a;
  --yellow:#ffd51f;
  --green:#1fb24a;
  --blue:#1d8fe0;
  --pink:#e5318c;
  --orange:#f7941d;
  --purple:#7b3fb5;
  --muted:#6b6b6b;
}
*{box-sizing:border-box;margin:0;padding:0}
html,body{width:1200px;height:2324px;overflow:hidden;background:var(--white)}
body{font-family:'Open Sans',sans-serif;color:var(--ink)}
.page{position:relative;width:1200px;height:2324px;overflow:hidden}
.abs{position:absolute}

/* header */
.brand{left:24px;top:18px;display:flex;align-items:center;gap:10px}
.brand-mark{width:44px;height:44px;background:var(--ink)}
.brand-name{font-family:'Baloo 2',cursive;font-weight:800;font-size:30px;line-height:1;color:var(--ink)}
.main-nav{right:60px;top:44px;display:flex;gap:26px;font-family:'Montserrat',sans-serif;font-weight:700;font-size:13px;letter-spacing:.5px}
.main-nav a{color:var(--ink);text-decoration:none}
.main-nav a.active{color:var(--red)}

/* hero */
.hero{left:0;top:80px;width:1200px;height:500px}
.hero-title{left:0;top:98px;width:1200px;text-align:center;font-family:'Baloo 2',cursive;font-weight:800;font-size:64px;line-height:56px;color:var(--ink)}
.hero-title .tag{position:absolute;left:880px;top:-30px;font-size:48px}

/* buttons */
.cta-row{left:120px;top:620px;width:960px;display:flex;justify-content:space-between}
.cta{position:relative;width:260px;height:64px;background:var(--ink);color:var(--yellow);font-family:'Montserrat',sans-serif;font-weight:800;font-size:15px;line-height:19px;text-align:center;display:flex;align-items:center;justify-content:center;overflow:hidden}
.cta::before{content:"";position:absolute;left:-14px;top:-14px;width:40px;height:40px;background:var(--green);transform:rotate(45deg)}
.cta::after{content:"";position:absolute;right:-14px;bottom:-14px;width:40px;height:40px;background:var(--blue);transform:rotate(45deg)}
.cta:nth-child(2)::before{background:var(--pink)}
.cta:nth-child(2)::after{background:var(--yellow)}
.cta:nth-child(3)::before{background:var(--orange)}
.cta:nth-child(3)::after{background:var(--red)}

/* features */
.features{left:100px;top:728px;width:1000px;display:flex;justify-content:space-between}
.feature{width:190px}
.feature-icon{width:46px;height:46px;display:flex;align-items:center;justify-content:center;margin-bottom:8px}
.feature-text{font-family:'Montserrat',sans-serif;font-size:12px;line-height:15px;font-weight:600;text-transform:uppercase}
.feature-text b{font-weight:800}

/* featured products */
.section-title{left:0;width:1200px;text-align:center;font-family:'Montserrat',sans-serif;font-weight:800;font-size:20px;letter-spacing:.5px}
.products{left:110px;top:890px;width:980px;display:flex;justify-content:space-between}
.product-card{width:300px;height:210px;background:var(--card)}

/* testimonials */
.testimonials{left:0;top:1650px;width:1200px;height:540px;background:var(--grey-bg)}
.testimonial{left:340px;width:520px}
.testimonial h3{font-family:'Open Sans',sans-serif;font-weight:700;font-size:15px;margin-bottom:4px}
.testimonial p{font-size:12px;line-height:17px;color:var(--muted)}
.swirl-left{left:0;top:1720px;width:210px;height:470px}
.swirl-right{left:1000px;top:1820px;width:200px;height:370px}

/* footer */
.footer-nav{left:0;top:2220px;width:1200px;display:flex;justify-content:center;gap:36px;font-family:'Montserrat',sans-serif;font-weight:700;font-size:12px;align-items:center}
.footer-nav a{color:var(--ink);text-decoration:none}
.social{display:flex;gap:10px}
.social span{width:16px;height:16px;background:var(--ink);display:block}
.legal{left:0;top:2262px;width:1200px;text-align:center;font-size:11px;color:var(--muted)}
</style>
</head>
<body>
<div class="page">

  <header>
    <div class="abs brand"><span class="brand-mark"></span><span class="brand-name">Bright Pouches</span></div>
    <nav class="abs main-nav">
      <a class="active" href="#">HOME</a><a href="#">ABOUT US</a><a href="#">BROWSE OUR DESIGNS</a><a href="#">SIGN IN</a><a href="#">CONTACT US</a>
    </nav>
  </header>

  <section class="abs hero">
    <svg width="1200" height="500" viewBox="0 0 1200 500">
      <defs>
        <linearGradient id="g-photo" x1="0" y1="0" x2="1" y2="1"><stop offset="0" stop-color="#9cc7e8"/><stop offset="1" stop-color="#e0b48c"/></linearGradient>
        <linearGradient id="g-wallet" x1="0" y1="0" x2="1" y2="0"><stop offset="0" stop-color="#c99a78"/><stop offset=".5" stop-color="#8fb9de"/><stop offset=".75" stop-color="#ffd51f"/><stop offset="1" stop-color="#e5318c"/></linearGradient>
        <linearGradient id="g-phone" x1="0" y1="0" x2="0" y2="1"><stop offset="0" stop-color="#ffd51f"/><stop offset=".5" stop-color="#1d8fe0"/><stop offset="1" stop-color="#e5318c"/></linearGradient>
        <radialGradient id="g-splash"><stop offset="0" stop-color="#ffd51f"/><stop offset=".5" stop-color="#1fb24a"/><stop offset="1" stop-color="#1d8fe0" stop-opacity="0"/></radialGradient>
      </defs>
      <polygon points="0,330 560,150 600,250 0,460" fill="var(--green)"/>
      <polygon points="640,200 1200,330 1200,440 640,300" fill="var(--yellow)"/>
      <rect x="40" y="40" width="220" height="200" fill="url(#g-splash)" role="img" aria-label="Colourful paint splash decoration"/>
      <rect x="880" y="320" width="320" height="170" fill="url(#g-splash)" role="img" aria-label="Colourful paint splash decoration"/>
      <g role="img" aria-label="Instant photo print of a smiling family">
        <rect x="40" y="160" width="150" height="170" fill="var(--white)" stroke="#d8d8d8" transform="rotate(-6 115 245)"/>
        <rect x="52" y="172" width="126" height="120" fill="url(#g-photo)" transform="rotate(-6 115 245)"/>
      </g>
      <path d="M200 350 q40 40 80 10" fill="none" stroke="var(--ink)" stroke-width="3"/>
      <rect x="280" y="200" width="590" height="220" rx="6" fill="url(#g-wallet)" role="img" aria-label="Open custom printed leather wallet showing a family photo and colourful paint design"/>
      <path d="M870 110 q30 -10 50 20" fill="none" stroke="var(--ink)" stroke-width="3"/>
      <g role="img" aria-label="Smartphone showing the wallet design editor">
        <rect x="920" y="40" width="160" height="310" rx="20" fill="#e6e6e6" stroke="#bdbdbd"/>
        <rect x="930" y="80" width="140" height="230" fill="url(#g-phone)"/>
      </g>
    </svg>
  </section>
  <h1 class="abs hero-title">funk up<br>your wallet.</h1>

  <nav class="abs cta-row">
    <a class="cta">CUSTOMISE<br>YOUR OWN WALLET</a>
    <a class="cta">EDIT<br>OUR TEMPLATES</a>
    <a class="cta">BESPOKE<br>DESIGNER WALLETS</a>
  </nav>

  <section class="abs features">
    <div class="feature">
      <div class="feature-icon" style="background:var(--green)"><svg width="26" height="26" viewBox="0 0 26 26"><path d="M13 2 L23 6 V13 C23 19 18 23 13 24 C8 23 3 19 3 13 V6 Z" fill="none" stroke="#fff" stroke-width="2.5"/><path d="M8 13 l4 4 l6 -8" fill="none" stroke="#fff" stroke-width="2.5"/></svg></div>
      <div class="feature-text"><b>5 year money back</b> guarantee on wallet</div>
    </div>
    <div class="feature">
      <div class="feature-icon" style="background:var(--yellow)"><svg width="26" height="26" viewBox="0 0 26 26"><circle cx="13" cy="10" r="7" fill="none" stroke="#fff" stroke-width="2.5"/><path d="M8 16 L6 24 L13 21 L20 24 L18 16" fill="none" stroke="#fff" stroke-width="2.5"/></svg></div>
      <div class="feature-text"><b>High quality,</b> durable leather, made to last</div>
    </div>
    <div class="feature">
      <div class="feature-icon" style="background:var(--blue)"><svg width="26" height="26" viewBox="0 0 26 26"><path d="M13 3 L23 8 V18 L13 23 L3 18 V8 Z M3 8 L13 13 L23 8 M13 13 V23" fill="none" stroke="#fff" stroke-width="2.2"/></svg></div>
      <div class="feature-text"><b>3D mockup</b> of the wallet as you are designing</div>
    </div>
    <div class="feature">
      <div class="feature-icon" style="background:var(--red)"><svg width="26" height="26" viewBox="0 0 26 26"><path d="M5 21 L7 15 L18 4 L22 8 L11 19 Z" fill="none" stroke="#fff" stroke-width="2.5"/></svg></div>
      <div class="feature-text"><b>Edit any</b> of our ready made wallet designs</div>
    </div>
    <div class="feature">
      <div class="feature-icon" style="background:var(--pink)"><svg width="26" height="26" viewBox="0 0 26 26"><rect x="3" y="6" width="20" height="15" fill="none" stroke="#fff" stroke-width="2.2"/><path d="M13 17 V9 M9 12 l4 -4 l4 4" fill="none" stroke="#fff" stroke-width="2.2"/></svg></div>
      <div class="feature-text"><b>Upload your photo</b> and edit them online with our online picture editor</div>
    </div>
  </section>

  <h2 class="abs section-title" style="top:846px">FEATURED PRODUCTS</h2>
  <section class="abs products">
    <div class="product-card"></div><div class="product-card"></div><div class="product-card"></div>
  </section>

  <section class="abs" style="left:0;top:1320px;width:1200px;height:300px">
    <svg width="1200" height="300" viewBox="0 0 1200 300">
      <defs>
        <linearGradient id="g-circle" x1="0" y1="0" x2="1" y2="1"><stop offset="0" stop-color="#555"/><stop offset="1" stop-color="#bbb"/></linearGradient>
      </defs>
      <g stroke="var(--ink)" stroke-width="2" fill="none">
        <polyline points="420,40 480,40 540,110"/>
        <polyline points="400,150 530,150"/>
        <polyline points="420,260 480,260 540,190"/>
        <polyline points="780,40 720,40 660,110"/>
        <polyline points="800,150 670,150"/>
        <polyline points="780,260 720,260 660,190"/>
      </g>
      <rect x="525" y="95" width="150" height="110" fill="url(#g-wallet)" role="img" aria-label="Wallet with colourful world map print"/>
      <g role="img" aria-label="Close-up photos of wallet details in circles">
        <circle cx="385" cy="40" r="36" fill="url(#g-circle)" stroke="var(--yellow)" stroke-width="6"/>
        <circle cx="360" cy="150" r="36" fill="url(#g-circle)" stroke="var(--red)" stroke-width="6"/>
        <circle cx="385" cy="260" r="36" fill="url(#g-circle)" stroke="var(--green)" stroke-width="6"/>
        <circle cx="815" cy="40" r="36" fill="url(#g-circle)" stroke="var(--blue)" stroke-width="6"/>
        <circle cx="840" cy="150" r="36" fill="url(#g-circle)" stroke="var(--orange)" stroke-width="6"/>
        <circle cx="815" cy="260" r="36" fill="url(#g-circle)" stroke="var(--pink)" stroke-width="6"/>
      </g>
    </svg>
  </section>

  <section class="abs testimonials"></section>
  <div class="abs swirl-left" role="img" aria-label="Colourful swirling cloud pattern" style="background:linear-gradient(160deg,var(--yellow),var(--red) 35%,var(--blue) 65%,var(--green))"></div>
  <div class="abs swirl-right" role="img" aria-label="Colourful swirling cloud pattern" style="background:linear-gradient(200deg,var(--pink),var(--yellow) 40%,var(--blue) 70%,var(--green))"></div>
  <h2 class="abs section-title" style="top:1676px;font-size:18px">WHAT THEY SAY ABOUT US</h2>
  <article class="abs testimonial" style="top:1740px">
    <h3>Lorem Ipsum Dolor</h3>
    <p>sit amet, consectetur adipiscing elit, sed do eiusmod tempor incididunt ut labore et dolore magna aliqua. Ut enim ad minim veniam, quis nostrud exercitation ullamco laboris nisi ut aliquip ex ea commodo consequat.</p>
  </article>
  <article class="abs testimonial" style="top:1880px">
    <h3>Lorem Ipsum Dolor</h3>
    <p>sit amet, consectetur adipiscing elit, sed do eiusmod tempor incididunt ut labore et dolore magna aliqua. Ut enim ad minim veniam, quis nostrud exercitation ullamco laboris nisi ut aliquip ex ea commodo consequat.</p>
  </article>
  <article class="abs testimonial" style="top:2020px">
    <h3>Lorem Ipsum Dolor</h3>
    <p>sit amet, consectetur adipiscing elit, sed do eiusmod tempor incididunt ut labore et dolore magna aliqua. Ut enim ad minim veniam, quis nostrud exercitation ullamco laboris nisi ut aliquip ex ea commodo consequat.</p>
  </article>
  <svg class="abs" style="left:588px;top:2150px" width="24" height="14" viewBox="0 0 24 14"><path d="M2 2 L12 11 L22 2" fill="none" stroke="#9a9a9a" stroke-width="2.5"/></svg>

  <footer>
    <nav class="abs footer-nav">
      <a href="#">HOME</a><a href="#">ABOUT US</a><a href="#">BROWSE OUR DESIGNS</a><a href="#">SIGN IN</a><a href="#">CONTACT US</a>
      <span class="social"><span></span><span></span><span></span></span>
    </nav>
    <p class="abs legal">Terms of Use &nbsp;·&nbsp; Privacy Policy &nbsp;·&nbsp; © 2018 Bright Pouches All rights reserved</p>
  </footer>

</div>
</body>
</html>
```